Landing Page for pellowick.ca Design To Inspire Confidence Playfulness and Optimised for Conversion

A Landing Page that will have a cheery playful demeanor all the while inspiring confidence to customers to trust us when they are shipping their used or broken electronics to us.
We are a startup looking to scale up our operations and we recently have been working on a website pellowick.ca. We want to improve on our current landing page. Competition includes tarnbloom.com , http://www.quorvela.com/ , spindrel.com but spindrel operates a little different then us.
We've done a bit of research and found the current landing page is not suited for conversions.
We want the design to work within our current landing page design and not interfere with major programing. So where the pictures of the phones are, beneath the search bar, we want the background changed and replaced with a creative call to action to click one of the devices to continue towards getting a quote and for this background to be appealing. Also we wanted to make the rest of the page beneath that more appealing and professional. A big issue for us is making sure whatever design is submitted can be easily integrated using our current platform.
We will try and answer any questions as promptly as possible and encourage it.
Updates
Industry/Entity Type
Shipping
Number of Pages Required
1 page
Look and feel
Each slider illustrates characteristics of the customer's brand and the style your logo design should communicate.

```html
<!DOCTYPE html>
<html lang="en">
<head>
<meta charset="utf-8">
<title>Pellowick – Sell Your Device</title>
<link href="https://fonts.googleapis.com/css2?family=Ubuntu:wght@400;500;700&display=swap" rel="stylesheet">
<style>
:root{
  --blue:#1e9ad6;
  --blue-dark:#167fb3;
  --ink:#333;
  --muted:#666;
  --band:#f2f2f2;
  --footer:#121212;
  --white:#fff;
  --nav:#1a1326;
}
*{box-sizing:border-box;margin:0;padding:0}
html,body{width:685px;height:1200px;overflow:hidden}
body{position:relative;background:var(--white);font-family:'Ubuntu',sans-serif;color:var(--ink)}
.abs{position:absolute}

/* header */
.site-header{left:0;top:0;width:685px;height:44px;background:var(--white)}
.brand{left:120px;top:12px;display:flex;align-items:center;gap:6px;color:var(--blue);font-weight:500;font-size:15px;letter-spacing:.5px}
.brand-mark{width:12px;height:12px;background:var(--blue)}
.search{left:217px;top:15px;width:241px;height:19px;border:1px solid #ccc;border-radius:2px;font-size:6px;color:#999;padding:5px 8px}
.search-btn{left:409px;top:15px;width:49px;height:19px;background:var(--blue);color:var(--white);font-size:6.5px;font-weight:500;display:flex;align-items:center;justify-content:center;gap:3px;border-radius:0 2px 2px 0}
.track{left:476px;top:21px;font-size:6.5px;font-weight:500;color:#222}
.login{left:528px;top:18px;width:44px;height:15px;background:var(--blue);color:var(--white);font-size:6.5px;font-weight:500;display:flex;align-items:center;justify-content:center}

/* hero */
.hero{left:0;top:44px;width:685px;height:367px;background:
  radial-gradient(circle at 88% 62%,rgba(230,30,50,.9) 0,rgba(230,30,50,0) 22%),
  radial-gradient(circle at 15% 40%,rgba(200,60,150,.85) 0,rgba(200,60,150,0) 28%),
  radial-gradient(circle at 50% 35%,rgba(90,120,240,.9) 0,rgba(90,120,240,0) 45%),
  linear-gradient(90deg,#3a1452 0%,#4b2a8e 35%,#3b46c8 55%,#2a1666 78%,#3a0c3a 100%)}
.main-nav{left:114px;top:1px;width:457px;height:41px;background:var(--nav);display:flex;align-items:center;padding-left:20px;gap:0;font-size:6.8px;font-weight:500;color:var(--white)}
.main-nav span{margin-right:14px}
.main-nav .active{color:var(--blue)}
.device{top:78px;border-radius:8px;background:linear-gradient(180deg,#2c2c30,#111)}
.device .screen{position:absolute;left:6px;right:6px;top:22px;bottom:22px;border-radius:2px}
.hero-title{left:0;top:263px;width:685px;text-align:center;color:var(--white);font-size:13px;font-weight:500}
.quote-btn{left:267px;top:295px;width:151px;height:26px;background:linear-gradient(180deg,#2fb3e8,#1893c9);border-radius:3px;color:var(--white);font-size:11px;display:flex;align-items:center;justify-content:center;box-shadow:0 6px 8px -4px rgba(0,0,0,.45)}
.dots{left:320px;top:349px;display:flex;gap:6px}
.dots i{width:6px;height:6px;border:1px solid var(--white);border-radius:50%}
.dots i.on{border-color:var(--blue)}

/* how it works */
.section-title{left:0;width:685px;text-align:center;font-weight:500}
.how-title{top:434px;font-size:14px;color:var(--ink)}
.step{top:467px;width:138px;height:133px;background:var(--blue);color:var(--white);text-align:center}
.step svg{display:block;margin:18px auto 0}
.step h3{font-size:11px;font-weight:500;margin-top:10px}
.step p{font-size:5.8px;font-weight:500;line-height:1.5;margin:8px 8px 0}

/* testimonials */
.reviews{left:0;top:637px;width:685px;height:295px;background:var(--band)}
.reviews-title{top:657px;font-size:14px;color:var(--blue)}
.shade{width:138px;height:14px;background:radial-gradient(ellipse at 50% 0,rgba(0,0,0,.28),rgba(0,0,0,0) 70%)}
.shade.low{background:radial-gradient(ellipse at 50% 100%,rgba(0,0,0,.28),rgba(0,0,0,0) 70%)}
.review-phone{border-radius:5px}
.arrow{top:778px;width:8px;height:12px}
.qmark{top:830px;color:var(--blue);font-size:20px;font-weight:700;line-height:1}
.review-text{top:853px;width:128px;text-align:center;font-size:11.4px;font-weight:500;line-height:1.3;color:#333}

/* press */
.press-title{top:947px;font-size:7.5px;color:#333}
.press{top:978px;left:120px;width:444px;display:flex;justify-content:space-between;align-items:center;color:#444}
.press span{font-family:'Ubuntu',sans-serif;font-size:8.5px;font-weight:500}

/* footer */
.site-footer{left:0;top:1013px;width:685px;height:187px;background:var(--footer);color:var(--white)}
.f-head{font-size:6.5px;font-weight:500;color:var(--blue)}
.f-list{font-size:6.3px;line-height:14px}
.news-copy{right:121px;top:1057px;width:170px;text-align:right;font-size:6.8px;line-height:1.55}
.news-input{left:412px;top:1087px;width:104px;height:18px;background:var(--white)}
.news-btn{left:516px;top:1087px;width:48px;height:18px;background:var(--blue);font-size:6.5px;font-weight:500;display:flex;align-items:center;justify-content:center}
.social{top:1138px;width:12px;height:12px;border-radius:50%}
.copyright{left:120px;top:1177px;font-size:6.3px;font-weight:500}
.badge{top:1174px;width:57px;height:15px;background:#e9edf2;border:1px solid #9fb0c4}
</style>
</head>
<body>

<header class="abs site-header">
  <div class="abs brand"><span class="brand-mark"></span>Pellowick</div>
  <div class="abs search">Search Your Items</div>
  <div class="abs search-btn">
    <svg width="6" height="6" viewBox="0 0 10 10"><circle cx="4" cy="4" r="3" fill="none" stroke="#fff" stroke-width="1.6"/><path d="M6.3 6.3L9 9" stroke="#fff" stroke-width="1.8"/></svg>SEARCH
  </div>
  <div class="abs track">Track My Offers</div>
  <div class="abs login">LOGIN</div>
</header>

<section class="abs hero">
  <nav class="abs main-nav">
    <span class="active">HOW IT WORKS</span><span>FONEX</span><span>DROIDEN</span><span>BRAMBLEKEY</span><span>SLATEPAD</span><span>TUNEPOD</span><span>FAQ</span><span>BUSINESS SOLUTIONS</span><span>CONTACT</span>
  </nav>
  <div class="abs device" style="left:201px;width:85px;height:168px" role="img" aria-label="Keyboard smartphone showing its message hub">
    <div class="screen" style="background:linear-gradient(180deg,#3b4f8a,#2a2f55)"></div>
  </div>
  <div class="abs device" style="left:305px;width:84px;height:168px;border-radius:11px" role="img" aria-label="Touchscreen smartphone showing app icons">
    <div class="screen" style="background:linear-gradient(180deg,#6aa6c9,#2f6a92)"></div>
  </div>
  <div class="abs device" style="left:407px;width:84px;height:168px;border-radius:10px;background:linear-gradient(180deg,#3a4150,#1a1e28)" role="img" aria-label="Large screen smartphone showing weather and clock">
    <div class="screen" style="top:16px;bottom:18px;background:linear-gradient(180deg,#7fb6de,#2d5f86)"></div>
  </div>
  <h1 class="abs hero-title">Your Not Just Selling Your Phone. Your Changing The World!</h1>
  <div class="abs quote-btn">GET A QUOTE</div>
  <div class="abs dots"><i class="on"></i><i></i><i></i><i></i></div>
</section>

<h2 class="abs section-title how-title">How It Works</h2>

<div class="abs step" style="left:120px">
  <svg width="30" height="34" viewBox="0 0 30 34"><path d="M2 1h18l8 8v24H2z" fill="#fff"/><path d="M20 1v8h8" fill="#cfe9f6"/><path d="M8 16h14M8 21h14M8 26h14" stroke="#1e9ad6" stroke-width="2"/></svg>
  <h3>Get A Quote</h3>
  <p>Choose your device, tell us its condition and get a quote for what we</p>
</div>
<div class="abs step" style="left:273px">
  <svg width="34" height="34" viewBox="0 0 34 34"><path d="M10 8h22v18H10z" fill="#fff"/><path d="M2 16l4-6h4v16H2z" fill="#fff"/><circle cx="8" cy="27" r="3.5" fill="#fff" stroke="#1e9ad6" stroke-width="1.5"/><circle cx="25" cy="27" r="3.5" fill="#fff" stroke="#1e9ad6" stroke-width="1.5"/></svg>
  <h3>Ship It Free</h3>
  <p>We pay for shipping.</p>
</div>
<div class="abs step" style="left:426px">
  <svg width="38" height="34" viewBox="0 0 38 34"><rect x="2" y="7" width="34" height="20" fill="#fff"/><rect x="6" y="11" width="26" height="12" fill="#1e9ad6"/><circle cx="19" cy="17" r="6" fill="#fff"/><text x="19" y="20.5" text-anchor="middle" font-size="9" font-weight="700" fill="#1e9ad6" font-family="Ubuntu,sans-serif">1</text></svg>
  <h3>Get Paid</h3>
  <p>We mail you cold, hard cash or choose an Parcelon gift card and get a bonus. will pay you.</p>
</div>

<section class="abs reviews"></section>
<h2 class="abs section-title reviews-title">What Canadians Are Saying About Pellowick</h2>

<div class="abs shade" style="left:122px;top:697px"></div>
<div class="abs shade" style="left:276px;top:697px"></div>
<div class="abs shade" style="left:424px;top:697px"></div>
<div class="abs review-phone" style="left:175px;top:717px;width:44px;height:85px;background:linear-gradient(180deg,#222,#3a1a2a 55%,#111)" role="img" aria-label="Slim black smartphone"></div>
<div class="abs review-phone" style="left:326px;top:716px;width:40px;height:85px;background:linear-gradient(180deg,#222,#4a6f8f 50%,#111)" role="img" aria-label="Touchscreen smartphone with app grid"></div>
<div class="abs review-phone" style="left:469px;top:712px;width:47px;height:92px;background:linear-gradient(180deg,#2a3140,#5c86b0 50%,#1d2230)" role="img" aria-label="Large smartphone with colourful wallpaper"></div>
<div class="abs shade low" style="left:122px;top:806px"></div>
<div class="abs shade low" style="left:276px;top:806px"></div>
<div class="abs shade low" style="left:424px;top:806px"></div>

<svg class="abs arrow" style="left:67px" viewBox="0 0 8 12"><path d="M6 1L2 6l4 5" fill="none" stroke="#888" stroke-width="1.4"/></svg>
<svg class="abs arrow" style="left:611px" viewBox="0 0 8 12"><path d="M2 1l4 5-4 5" fill="none" stroke="#888" stroke-width="1.4"/></svg>

<div class="abs qmark" style="left:121px">&ldquo;</div>
<div class="abs qmark" style="left:273px">&ldquo;</div>
<div class="abs qmark" style="left:426px">&ldquo;</div>
<p class="abs review-text" style="left:130px">Best thing that every happened to me to help me pay off my contract and start fresh....</p>
<p class="abs review-text" style="left:281px">Thanks thanks thanks, Ill be back to sell my daughters phone....</p>
<p class="abs review-text" style="left:429px">Please tell me how I just got paid this much....</p>

<h2 class="abs section-title press-title">As Featured In</h2>
<div class="abs press">
  <span>Harbor City Ledger</span><span>Crestline</span><span>Channel 9</span><span>Market Lantern</span><span>Bytefold</span><span>Valley Courier</span>
</div>

<footer class="abs site-footer"></footer>
<div class="abs f-head" style="left:120px;top:1039px">QUICK LINKS</div>
<div class="abs f-list" style="left:120px;top:1057px">How It Works<br>Fonex<br>Droiden<br>Bramblekey<br>Slatepad<br>Tunepod</div>
<div class="abs f-list" style="left:221px;top:1057px">Faq<br>Business Solutions<br>Contact</div>
<div class="abs f-head" style="left:310px;top:1039px">CONTACT US</div>
<div class="abs f-list" style="left:310px;top:1057px;color:#fff">418 Marlow Lane West<br>Easton Ontario, K2R 7P4<br>P.O Box #32</div>
<div class="abs f-head" style="left:440px;top:1039px;width:124px;text-align:right">SIGN UP FOR NEWSLETTER</div>
<p class="abs news-copy" style="color:#fff">Refer a friend, because friends don't let friends trash the planet</p>
<div class="abs news-input"></div>
<div class="abs news-btn">SUBSCRIBE</div>
<div class="abs f-head" style="left:440px;top:1120px;width:124px;text-align:right">CONNECT WITH US</div>
<div class="abs social" style="left:521px;background:#3b5a9a"></div>
<div class="abs social" style="left:537px;background:#35aee2"></div>
<svg class="abs social" style="left:553px" viewBox="0 0 12 12"><circle cx="6" cy="6" r="6" fill="#2aa55a"/><rect x="3" y="4" width="6" height="4.5" fill="#fff"/><path d="M3 4l3 2.5L9 4" fill="none" stroke="#2aa55a" stroke-width=".8"/></svg>
<div class="abs copyright">© 2015 Pellowick. All Rights Reserved | Terms &amp; Condition</div>
<div class="abs badge" style="left:448px"></div>
<div class="abs badge" style="left:507px"></div>

</body>
</html>
```